Extra job from Miami Logo design job

This posting is for the winner of the Lorvane Swim Shop logo, we need an example of what the commerce webpage would look like.

Please go here to submit the logo first:

http://jobs.pixelmarquee.com/job.aspx?id=512807.

Shop

```html
<!DOCTYPE html>
<html lang="en">
<head>
<meta charset="utf-8">
<title>Lorvane Swim Shop</title>
<link href="https://fonts.googleapis.com/css2?family=Open+Sans:wght@400;600&family=Josefin+Sans:wght@600;700&family=Playfair+Display&display=swap" rel="stylesheet">
<style>
:root{
  --pink:#f0589a;
  --pink-dark:#d8407f;
  --teal:#33c6d9;
  --teal-dark:#1fb3c8;
  --teal-light:#4fd2e2;
  --text:#555;
  --muted:#8a8a8a;
  --line:#dcdcdc;
  --white:#fff;
}
*{margin:0;padding:0;box-sizing:border-box}
html,body{width:889px;height:1200px;overflow:hidden}
body{position:relative;background:var(--white);font-family:"Open Sans",sans-serif;color:var(--text)}
.abs{position:absolute}
.header-bg{left:0;top:0;width:889px;height:416px;background:radial-gradient(circle at 30% 30%,#f6f6f6,#e9e9e9);border-top:1px dashed #ccc}
.top-links{right:140px;top:14px;font-size:10px;color:#666;word-spacing:2px}
.top-links span{margin:0 5px;color:#999}
.search{left:139px;top:50px;width:174px;height:21px;border:1px solid #ccc;border-radius:11px;background:var(--white);font-size:8px;font-style:italic;color:#888;padding:5px 11px}
.search svg{position:absolute;right:8px;top:4px}
.cart{left:684px;top:46px;display:flex;gap:5px;align-items:center}
.cart-text{font-size:7px;color:#888;line-height:1}
.cart-text b{display:block;font-size:10px;color:#333;font-weight:400;margin-top:2px}
.ribbon-end{top:94px;width:32px;height:36px;background:var(--pink-dark)}
.ribbon-end.left{left:107px;clip-path:polygon(0 0,100% 0,100% 100%,0 100%,12px 50%)}
.ribbon-end.right{left:751px;clip-path:polygon(0 0,100% 0,calc(100% - 12px) 50%,100% 100%,0 100%)}
.nav{left:137px;top:80px;width:615px;height:34px;background:var(--pink)}
.nav a{position:absolute;top:11px;font-size:11px;color:var(--white);text-decoration:none;text-transform:uppercase;letter-spacing:.2px}
.hero-card{left:138px;top:115px;width:620px;height:275px;background:var(--white);box-shadow:0 3px 6px rgba(0,0,0,.18)}
.hero-photo{left:143px;top:119px;width:602px;height:251px;background:linear-gradient(180deg,#c9b2b4 0%,#b79a9e 35%,#b58a82 60%,#9a6c62 100%);display:flex;flex-direction:column;align-items:center;justify-content:center;text-align:center;color:var(--white);font-family:"Josefin Sans",sans-serif}
.hero-photo h1{font-size:26px;font-weight:700;letter-spacing:2.5px;margin-top:-10px}
.hero-photo p{font-size:13px;font-weight:700;letter-spacing:2px;margin-top:2px}
.logo{left:374px;top:26px;width:124px;height:124px;border-radius:50%;background:var(--teal);border:4px solid var(--white);display:flex;align-items:center;justify-content:center;text-align:center;color:var(--white);box-shadow:0 2px 4px rgba(0,0,0,.15)}
.logo-name{font-size:15px;line-height:1.25;font-weight:400;margin-top:8px}
.dots{left:430px;top:391px;display:flex;gap:3px}
.dots i{width:9px;height:9px;border-radius:50%;background:#444}
.features{left:137px;top:434px;width:615px;display:flex;gap:8px}
.feature{width:199px;text-align:center}
.feature-img{height:96px}
.feature h2{font-family:"Playfair Display",serif;font-weight:400;font-size:14px;color:var(--pink);margin-top:11px;text-transform:uppercase}
.feature p{font-size:7.5px;line-height:1.6;color:var(--muted);margin-top:2px;padding:0 8px}
.divider{left:145px;top:613px;width:604px;border-top:1px dotted #888}
.section-ribbon{left:347px;top:648px;width:190px;height:34px}
.section-ribbon span{position:absolute;left:25px;top:0;width:140px;height:30px;background:var(--teal);color:#123;font-family:"Josefin Sans",sans-serif;font-weight:600;font-size:13px;letter-spacing:1.5px;text-align:center;line-height:33px}
.products{left:139px;top:699px;width:615px;height:227px;border:1px solid var(--line);display:flex}
.product{flex:1;border-left:1px solid var(--line);text-align:center;padding-top:8px}
.product:first-child{border-left:none}
.product-img{width:80px;height:126px;margin:0 auto;border-radius:40px 40px 6px 6px}
.product h3{font-weight:400;font-size:12px;color:#444;margin-top:9px;letter-spacing:.3px}
.product p{font-size:7.5px;line-height:1.6;color:var(--muted);margin-top:2px;padding:0 12px}
.buy{display:inline-block;margin-top:8px;width:70px;height:20px;background:var(--pink);color:var(--white);font-size:8.5px;font-weight:600;line-height:20px;clip-path:polygon(0 0,100% 0,94% 50%,100% 100%,0 100%,6% 50%)}
.footer{left:0;top:958px;width:889px;height:202px;background:linear-gradient(180deg,var(--teal-light),var(--teal));border-top:1px dashed rgba(255,255,255,.6)}
.footer-col{color:var(--white)}
.footer-col h4{font-weight:400;font-size:10.5px;text-transform:uppercase;margin-bottom:4px}
.footer-col li{list-style:none;font-size:8px;line-height:15px}
.newsletter p{font-size:8.5px}
.email{margin-top:8px;width:167px;height:20px;background:var(--white);display:flex;font-size:7px;color:#555}
.email span{flex:1;padding:6px 8px}
.email b{width:19px;background:#111;display:flex;align-items:center;justify-content:center}
.social{display:flex;gap:4px;margin-top:10px}
.social i{width:19px;height:19px;border-radius:50%;background:var(--white);opacity:.9}
.bottom-bar{left:0;top:1160px;width:889px;height:40px;background:var(--teal-dark);color:var(--white);font-size:8px;padding:14px 136px}
</style>
</head>
<body>
<div class="abs header-bg"></div>
<div class="abs top-links">My Account<span>|</span>My Wishlist<span>|</span>Checkout<span>|</span>Log In</div>
<div class="abs search">Search here..
  <svg width="11" height="11" viewBox="0 0 11 11"><circle cx="4.5" cy="4.5" r="3.5" fill="none" stroke="#999" stroke-width="1.2"/><line x1="7" y1="7" x2="10" y2="10" stroke="#999" stroke-width="1.2"/></svg>
</div>
<div class="abs cart">
  <svg width="26" height="26" viewBox="0 0 26 26"><rect x="2" y="8" width="22" height="17" fill="#333"/><path d="M8 8V5a5 5 0 0 1 10 0v3" fill="none" stroke="#333" stroke-width="1.5"/><path d="M9 14a4 4 0 0 0 8 0" fill="none" stroke="#fff" stroke-width="1.5"/></svg>
  <div class="cart-text">My Cart<b>0 items</b></div>
</div>

<div class="abs ribbon-end left"></div>
<div class="abs ribbon-end right"></div>
<nav class="abs nav">
  <a style="left:28px">Home</a>
  <a style="left:81px">Products</a>
  <a style="left:158px">About Us</a>
  <a style="left:383px">Top Selling</a>
  <a style="left:469px">Service</a>
  <a style="left:532px">Specials</a>
</nav>

<div class="abs hero-card"></div>
<div class="abs hero-photo" role="img" aria-label="Photo of a woman in a summer dress sitting on a sandy beach at sunset">
  <h1>MAIMI BEST BRANDED BIKINI</h1>
  <p>MAURIS VEL LACUS VITAE FELIS VOLUTPAT</p>
</div>

<div class="abs logo">
  <div class="logo-name">Lorvane<br>Swim Shop</div>
</div>

<div class="abs dots"><i></i><i></i><i></i><i></i></div>

<section class="abs features">
  <div class="feature">
    <div class="feature-img" role="img" aria-label="Photo of a woman in a patterned bandeau bikini by a pool" style="background:linear-gradient(135deg,#3d6fa8,#c98a6e 55%,#e0c0b0)"></div>
    <h2>Simple Installation</h2>
    <p>Vivamus porttitor purus nisi eleifend libero a tempus libero lectus feugiat felis Morbi diam mauris</p>
  </div>
  <div class="feature">
    <div class="feature-img" role="img" aria-label="Photo of a woman in a dark bikini lying on the beach" style="background:linear-gradient(180deg,#9fc5d8,#d9e4e8 55%,#b8a6a0)"></div>
    <h2>Best Collections</h2>
    <p>Vivamus porttitor purus nisi eleifend libero a tempus libero lectus feugiat felis Morbi diam mauris</p>
  </div>
  <div class="feature">
    <div class="feature-img" role="img" aria-label="Photo of a woman in a black bikini and sunglasses on a beach towel" style="background:linear-gradient(180deg,#6fa4c8,#bcd3df 55%,#e8e6e4)"></div>
    <h2>Branded Products</h2>
    <p>Vivamus porttitor purus nisi eleifend libero a tempus libero lectus feugiat felis Morbi diam mauris</p>
  </div>
</section>

<div class="abs divider"></div>

<div class="abs section-ribbon">
  <svg width="190" height="34" viewBox="0 0 190 34" style="position:absolute;left:0;top:0">
    <polygon points="0,6 30,6 30,34 0,34 8,20" fill="#27b7cb"/>
    <polygon points="160,6 190,6 182,20 190,34 160,34" fill="#27b7cb"/>
    <polygon points="25,30 40,30 40,34" fill="#168a9a"/>
    <polygon points="150,30 165,30 150,34" fill="#168a9a"/>
  </svg>
  <span>NEW ARRIVALS</span>
</div>

<section class="abs products">
  <div class="product">
    <div class="product-img" role="img" aria-label="Product photo of a model in a pink bikini" style="background:linear-gradient(180deg,#e9ddd6,#ff5aa4 60%,#f3e6e0)"></div>
    <h3>PINK BIKINI</h3>
    <p>Vivamus porttitor purus nisi eleif-<br>end libero a tempus libero</p>
    <span class="buy">BUY NOW</span>
  </div>
  <div class="product">
    <div class="product-img" role="img" aria-label="Product photo of a model in a black lace bikini" style="background:linear-gradient(180deg,#e3d3c8,#3a3232 60%,#efe4dc)"></div>
    <h3>BLACK BIKINI</h3>
    <p>Vivamus porttitor purus nisi eleif-<br>end libero a tempus libero</p>
    <span class="buy">BUY NOW</span>
  </div>
  <div class="product">
    <div class="product-img" role="img" aria-label="Product photo of a model in a red bikini" style="background:linear-gradient(180deg,#e9ddd6,#f04a6a 60%,#f3e6e0)"></div>
    <h3>RED BIKINI</h3>
    <p>Vivamus porttitor purus nisi eleif-<br>end libero a tempus libero</p>
    <span class="buy">BUY NOW</span>
  </div>
  <div class="product">
    <div class="product-img" role="img" aria-label="Product photo of a model in an orange bikini" style="background:linear-gradient(180deg,#e9ddd6,#f2554e 60%,#f3e6e0)"></div>
    <h3>ORANGE BIKINI</h3>
    <p>Vivamus porttitor purus nisi eleif-<br>end libero a tempus libero</p>
    <span class="buy">BUY NOW</span>
  </div>
</section>

<footer class="abs footer"></footer>
<div class="abs footer-col" style="left:139px;top:993px">
  <h4>Our Offers</h4>
  <ul><li>New products</li><li>Top sellers</li><li>Specials</li><li>Manufacturers</li><li>Suppliers</li><li>Specials</li><li>Service</li></ul>
</div>
<div class="abs footer-col" style="left:239px;top:993px">
  <h4>Shipping Info</h4>
  <ul><li>Returns</li><li>Delivery</li><li>Service</li><li>Gift Cards</li><li>Mobile</li><li>Gift Cards</li><li>Manufacturers</li></ul>
</div>
<div class="abs footer-col" style="left:350px;top:993px">
  <h4>Our Account</h4>
  <ul><li>Your Account</li><li>Information</li><li>Addresses</li><li>Discount</li><li>Orders history</li><li>Addresses</li><li>Search Terms</li></ul>
</div>
<div class="abs footer-col" style="left:462px;top:993px">
  <h4>Our Support</h4>
  <ul><li>Site Map</li><li>Search Terms</li><li>Advanced Search</li><li>Mobile</li><li>Contact Us</li><li>Mobile</li><li>Addresses</li></ul>
</div>
<div class="abs footer-col newsletter" style="left:568px;top:993px">
  <h4>Sign Up Our Newsletter</h4>
  <p>Please Sign up here for latest offers.</p>
  <div class="email"><span>Email address</span><b><svg width="6" height="8" viewBox="0 0 6 8"><polygon points="0,0 6,4 0,8" fill="#fff"/></svg></b></div>
  <div class="social"><i></i><i></i><i></i><i></i></div>
</div>

<div class="abs bottom-bar">© 2014 Company Name &nbsp;All right reserved &nbsp;Term of Use</div>
</body>
</html>
```